Our Company name is Bluefield Office Cleaning Services. We are a Toronto(GTA) company looking for a brochure that with Logo design that gives a description of what we do.

We are a company that specializes in cleaning and sanitizing office/ workplaces. Our Experience includes working with school boards and hospitals, and have 15 plus years experience. We are looking for a simple design that catches and explains to our customers what we offer with some pics, which you can provide.

if you have any questions please let us know.

thank you

Target Market(s)

We are focusing Businesses

Font styles to use
Serif

Colors

Designer to choose colors to be used in the design.

Requirements
Must have
• Must have our name/Logo, brief description of what we do. Contact numbers, (416)-555-0183/ (647)555-0927 email (bluefieldofficecleaningservices@mailbox-example.com
• Pics which you can provide
Nice to have
• We trust your imagination on this

```html
<!DOCTYPE html>
<html lang="en">
<head>
<meta charset="utf-8">
<title>Bluefield Office Cleaning Services – Brochure</title>
<link rel="stylesheet" href="https://fonts.googleapis.com/css2?family=Montserrat:ital,wght@0,600;0,700;1,600;1,700&family=Open+Sans:wght@400;600;700&display=swap">
<style>
:root{
  --blue:#1d86c6;
  --blue-dark:#135e95;
  --green:#5db530;
  --sky:#dcecf6;
  --ink:#3b5a73;
  --paper:#ffffff;
  --stage:#f1f3f5;
}
*{box-sizing:border-box;margin:0;padding:0}
html,body{width:811px;height:1200px;overflow:hidden;background:var(--stage)}
body{position:relative;font-family:"Open Sans",sans-serif;color:var(--ink)}
.spread{position:absolute;background:var(--paper);box-shadow:0 2px 8px rgba(0,0,0,.18);overflow:hidden;display:flex}
.spread--outside{left:64px;top:14px;width:708px;height:574px}
.spread--inside{left:28px;top:605px;width:756px;height:575px}
.panel{position:relative;flex:1;height:100%;overflow:hidden}
.photo{position:absolute}
.wave{position:absolute;left:0;width:100%}
.heading{font-family:"Montserrat",sans-serif;font-style:italic;font-weight:700;color:var(--green)}
.body-copy{font-size:9.5px;line-height:1.45;color:var(--ink)}

/* outside – left panel */
.features{position:absolute;left:0;top:0;width:100%;height:250px}
.features__tint{position:absolute;inset:0;background:linear-gradient(160deg,rgba(29,134,198,.55),rgba(93,181,48,.35)),linear-gradient(180deg,#b9cfd9,#e9eef0)}
.features__list{position:absolute;left:20px;top:40px;list-style:none;color:#fff;font-size:9.5px;font-weight:600;line-height:1.3}
.features__list li{position:relative;padding-left:13px;margin-bottom:10px}
.features__list li::before{content:"";position:absolute;left:0;top:4px;width:6px;height:6px;background:var(--green);border-radius:50%}

/* outside – middle */
.intro__title{position:absolute;left:16px;right:16px;top:20px;text-align:center;font-family:"Montserrat",sans-serif;font-weight:700;font-size:12px;line-height:1.3;color:var(--blue)}
.intro__text{position:absolute;left:16px;right:16px;top:72px;text-align:center;color:var(--blue);font-size:9px;line-height:1.3}
.contact{position:absolute;left:0;right:0;top:388px;text-align:center}
.contact__title{font-size:20px}
.contact__phone{font-family:"Montserrat",sans-serif;font-weight:700;font-size:19px;color:var(--blue);line-height:1.25}
.contact__email{font-size:6.6px;color:var(--blue-dark);margin-top:4px}
.brand{display:flex;align-items:center;gap:6px;justify-content:center}
.brand__dot{width:22px;height:22px;border-radius:50%;background:var(--blue);flex:none}
.brand__name{font-family:"Open Sans",sans-serif;font-weight:700;color:var(--blue);line-height:1.05;text-transform:uppercase;text-align:left}

/* outside – right */
.badge{position:absolute;right:0;top:0;width:92px;height:64px;background:var(--blue);border-bottom-left-radius:40px;color:#fff;text-align:center;padding-top:12px;font-family:"Montserrat",sans-serif;font-weight:700;font-size:12px;line-height:1.1}
.badge small{display:block;font-size:8px;color:#c9f0b5}
.tagline{position:absolute;left:0;right:0;bottom:30px;text-align:center;font-family:"Montserrat",sans-serif;font-style:italic;font-weight:700;font-size:11px;color:var(--blue)}

/* inside */
.about__title{position:absolute;left:22px;top:334px;font-size:22px;color:#fff}
.about__text{position:absolute;left:22px;right:22px;top:378px}
.about__text p{margin-bottom:8px}
.section-title{position:absolute;left:0;right:0;top:38px;text-align:center;font-size:22px}
.section-body{position:absolute;left:24px;right:22px;top:82px}
.checklist{list-style:none;margin-top:8px}
.checklist li{position:relative;padding-left:13px;margin-bottom:7px;font-size:9.5px}
.checklist li::before{content:"";position:absolute;left:0;top:4px;width:6px;height:6px;background:var(--green);border-radius:50%}
.benefits p{margin-bottom:10px;text-align:center}
</style>
</head>
<body>

<section class="spread spread--outside">
  <div class="panel panel--features">
    <div class="features" role="img" aria-label="Bright open office interior with blue tint">
      <div class="features__tint"></div>
    </div>
    <ul class="features__list">
      <li>Local Commercial Cleaning Company</li>
      <li>Licensed, Bonded &amp; Insured</li>
      <li>24/7 Cleaning Service &amp; Support</li>
      <li>Reliable employees</li>
      <li>Over 15 years of satisfied customers</li>
      <li>100% Satisfaction on EVERY JOB Guarantee!</li>
    </ul>
    <div class="photo" style="left:0;top:250px;width:100%;height:324px;background:linear-gradient(180deg,#eef1f3,#c8d3da 60%,#9fb0bb)" role="img" aria-label="Clean modern office with desks and chairs"></div>
    <svg class="wave" style="top:228px;height:40px" viewBox="0 0 236 40" preserveAspectRatio="none"><path d="M0 22 Q118 0 236 18 L236 40 L0 40Z" fill="var(--green)"/></svg>
  </div>

  <div class="panel panel--intro">
    <h2 class="intro__title">LET OUR<br>OFFICE CLEANING SERVICES<br>KEEP YOU LOOKING GOOD</h2>
    <p class="intro__text">At Bluefield Office Cleaning Services, we measure our success by that of our clients, and we truly believe that a cleaner, healthier work space helps a business thrive. We strive to attract new customers and increase productivity. As one of the leading office cleaning companies in the GTA, hiring Bluefield Office Cleaning will free you up to focus on your business without ever having to worry about how your office looks.</p>
    <div class="photo" style="left:0;top:262px;width:100%;height:114px;background:linear-gradient(135deg,#d6e2e9,#a9bfcc)" role="img" aria-label="Cleaner wiping an office chair"></div>
    <svg class="wave" style="top:252px;height:30px" viewBox="0 0 236 30" preserveAspectRatio="none"><path d="M0 0 L236 0 L236 8 Q118 30 0 10Z" fill="#fff"/><path d="M0 10 Q118 30 236 8 L236 12 Q118 34 0 14Z" fill="var(--blue)"/></svg>
    <svg class="wave" style="top:360px;height:24px" viewBox="0 0 236 24" preserveAspectRatio="none"><path d="M0 14 Q118 -4 236 12 L236 24 L0 24Z" fill="#fff"/></svg>
    <div class="contact">
      <h3 class="heading contact__title">Contact us</h3>
      <p class="contact__phone">(416)-555-0183<br>(647)555-0927</p>
      <p class="contact__email">bluefieldofficecleaningservices@mailbox-example.com</p>
      <div class="brand" style="margin-top:14px">
        <span class="brand__dot" style="width:18px;height:18px"></span>
        <span class="brand__name" style="font-size:9px">Bluefield<br>Office Cleaning Services</span>
      </div>
    </div>
  </div>

  <div class="panel panel--cover">
    <div class="photo" style="left:0;top:0;width:100%;height:370px;background:linear-gradient(160deg,#e7eef2,#b7c7d1)" role="img" aria-label="Cleaner mopping a bright office floor"></div>
    <svg class="wave" style="top:330px;height:60px" viewBox="0 0 236 60" preserveAspectRatio="none"><path d="M0 30 Q118 -6 236 20 L236 60 L0 60Z" fill="var(--green)"/><path d="M0 40 Q118 6 236 30 L236 60 L0 60Z" fill="#fff"/></svg>
    <div class="badge">15 YEARS<small>EXPERIENCE</small></div>
    <div class="brand" style="position:absolute;left:0;right:0;top:415px">
      <span class="brand__dot" style="width:30px;height:30px"></span>
      <span class="brand__name" style="font-size:15px">Bluefield<br><span style="font-size:8px">Office Cleaning Services</span></span>
    </div>
    <p class="tagline">LET US DO THE DIRTY WORK</p>
  </div>
</section>

<section class="spread spread--inside">
  <div class="panel panel--about">
    <div class="photo" style="left:0;top:0;width:100%;height:340px;background:linear-gradient(150deg,#f0f3f5,#c3d1da)" role="img" aria-label="Cleaner wiping an office desk"></div>
    <svg class="wave" style="top:300px;height:80px" viewBox="0 0 252 80" preserveAspectRatio="none"><path d="M0 20 Q140 -10 252 30 L252 80 L0 80Z" fill="var(--green)"/><path d="M0 28 Q140 0 252 38 L252 80 L0 80Z" fill="var(--blue)"/><path d="M0 70 Q126 60 252 76 L252 80 L0 80Z" fill="#fff"/></svg>
    <h2 class="heading about__title">About us</h2>
    <div class="about__text body-copy">
      <p>Bluefield Office Cleaning Services has more than 15 years of office cleaning experience working with a variety of companies as well as smaller independent businesses.</p>
      <p>Providing a clean office environment is a key element to a modern, effective organization. Cleanliness is of paramount importance to a company's brand persona and client perception. It also has a major role to play for employee health and wellbeing and might directly influence productivity through prevent absences from work.</p>
    </div>
  </div>

  <div class="panel panel--why">
    <h2 class="heading section-title">Why choose us</h2>
    <div class="section-body body-copy">
      <p>We provide an extensive range of office cleaning services including:</p>
      <ul class="checklist">
        <li>Window washing</li>
        <li>Spot cleaning (e.g. new spills)</li>
        <li>Cleaning air conditioning vents</li>
        <li>Cleaning cafeterias, staff rooms and kitchens</li>
        <li>Vacuuming carpets</li>
        <li>Emptying trash bins and replace bags every day</li>
        <li>Sanitizing door handles</li>
        <li>Dusting room fixtures on a weekly basis</li>
        <li>Blind cleaning</li>
        <li>Floor stripping and refinishing</li>
      </ul>
    </div>
  </div>

  <div class="panel panel--benefits">
    <h2 class="heading section-title">Benefits</h2>
    <div class="section-body body-copy benefits">
      <p>Employees in a clean, tidy office work more efficiently than they would in a messy environment. Also, potential clients who visit a clean office leave with a favourable impression of the place. An office that hires Bluefield Office Cleaning Services is taking a positive step toward maintaining a professional working environment.</p>
      <p>Our office cleaning service also allows your employees to focus on their work. Our office cleaners take care of all the important cleaning tasks that create a tidy office environment. Our office building cleaning service has the cleaning solutions and supplies to clean an office bathroom in an efficient, thorough way.</p>
      <p>We have all the right tools for effectively cleaning.</p>
    </div>
    <div class="photo" style="left:0;top:440px;width:100%;height:135px;background:linear-gradient(135deg,#d9e4ea,#9fb4c2)" role="img" aria-label="Cleaning team working in an office"></div>
    <svg class="wave" style="top:428px;height:30px" viewBox="0 0 252 30" preserveAspectRatio="none"><path d="M0 0 L252 0 L252 8 Q126 30 0 12Z" fill="#fff"/><path d="M0 12 Q126 30 252 8 L252 13 Q126 35 0 17Z" fill="var(--green)"/></svg>
  </div>
</section>

</body>
</html>
```